Harborlight Vitality Studio Business Cards and Stationary
Harborlight Vitality Studio
Harborlight Vitality Studio Business Cards and Stationary - Massage Therapy
Creative Brief
Use same font as used in my logo
Similar font as in the word Foundation, or whatever you feel is appropriate
Professional
Dr. Raymond Okafor, D.C.
Every Step Starts With Balance
none at the moment
877 Go Align (462-5446)
www.frontdesk@harborlightvitalitystudio.com
www.harborlightvitalitystudio.com
1.I would like my Logo on top 2. Every Step Starts With Balance 3. Dr. Raymond Okafor, D.C. 4. 877 Go Align (462-5446) 5.email the web site

```html
<!DOCTYPE html>
<html lang="en">
<head>
<meta charset="utf-8">
<title>Harborlight Vitality Studio Business Cards</title>
<link rel="stylesheet" href="https://fonts.googleapis.com/css2?family=Open+Sans:ital,wght@0,400;0,600;0,700;1,400&display=swap">
<style>
  :root {
    --backdrop: #e6e6e8;
    --card: #ffffff;
    --brand-blue: #1f6fb2;
    --brand-red: #c0272d;
    --accent-orange: #d8531f;
    --ink: #3a3a3a;
    --muted: #6b6b6b;
    --divider: #c9c9c9;
  }
  * { box-sizing: border-box; margin: 0; padding: 0; }
  html, body {
    width: 1200px; height: 864px; overflow: hidden;
    background: var(--backdrop);
    font-family: "Open Sans", Arial, sans-serif;
    color: var(--ink);
  }
  .stage {
    width: 1200px; height: 864px;
    display: flex; flex-direction: column;
    align-items: center; justify-content: center; gap: 40px;
  }
  .card {
    position: relative;
    width: 640px; height: 366px;
    background: var(--card);
    border-radius: 18px;
    overflow: hidden;
    box-shadow: 0 6px 18px rgba(0,0,0,0.12);
  }
  /* back of card */
  .card-back {
    display: flex; flex-direction: column;
    align-items: center; justify-content: center; gap: 34px;
  }
  .brand {
    display: flex; align-items: center; gap: 12px;
  }
  .brand-dot {
    width: 30px; height: 30px; border-radius: 50%;
    background: var(--brand-blue);
    flex: none;
  }
  .brand-name {
    font-weight: 700;
    font-size: 26px;
    color: var(--brand-blue);
    letter-spacing: 0.5px;
  }
  .back-web {
    font-size: 15px;
    letter-spacing: 3px;
    color: var(--brand-blue);
    font-weight: 600;
  }
  /* front of card */
  .card-front { padding: 56px 44px 0 40px; }
  .front-body {
    display: flex; align-items: center; gap: 26px;
  }
  .identity { width: 300px; }
  .identity .brand-name { font-size: 22px; }
  .identity .brand-dot { width: 26px; height: 26px; }
  .person {
    margin-top: 26px;
    font-size: 17px; font-weight: 700;
    color: var(--accent-orange);
  }
  .tagline {
    margin-top: 4px;
    font-size: 14px; font-style: italic;
    color: var(--muted);
  }
  .rule {
    width: 1px; height: 150px; background: var(--divider);
  }
  .contacts { list-style: none; display: flex; flex-direction: column; gap: 12px; }
  .contacts li {
    display: flex; align-items: center; gap: 9px;
    font-size: 11px; color: var(--ink);
    white-space: nowrap;
  }
  .icon {
    width: 20px; height: 20px; border-radius: 50%;
    background: var(--brand-red);
    display: flex; align-items: center; justify-content: center;
    flex: none;
  }
  .icon svg { width: 12px; height: 12px; }
  .swoosh { position: absolute; left: 0; bottom: 0; width: 640px; height: 110px; }
</style>
</head>
<body>
<main class="stage">
  <section class="card card-back" aria-label="Business card back">
    <div class="brand">
      <span class="brand-dot"></span>
      <span class="brand-name">Harborlight Vitality Studio</span>
    </div>
    <p class="back-web">www.harborlightvitalitystudio.com</p>
  </section>

  <section class="card card-front" aria-label="Business card front">
    <div class="front-body">
      <div class="identity">
        <div class="brand">
          <span class="brand-dot"></span>
          <span class="brand-name">Harborlight Vitality Studio</span>
        </div>
        <p class="person">Dr. Raymond Okafor, D.C.</p>
        <p class="tagline">Every Step Starts With Balance</p>
      </div>
      <div class="rule"></div>
      <ul class="contacts">
        <li>
          <span class="icon"><svg viewBox="0 0 24 24"><path fill="#fff" d="M6.6 10.8a15 15 0 0 0 6.6 6.6l2.2-2.2a1 1 0 0 1 1-.25 11.4 11.4 0 0 0 3.6.57 1 1 0 0 1 1 1V20a1 1 0 0 1-1 1A17 17 0 0 1 3 4a1 1 0 0 1 1-1h3.5a1 1 0 0 1 1 1c0 1.25.2 2.45.57 3.57a1 1 0 0 1-.25 1z"/></svg></span>
          877 Go Align (462-5446)
        </li>
        <li>
          <span class="icon"><svg viewBox="0 0 24 24"><rect x="3" y="6" width="18" height="12" rx="1.5" fill="#fff"/><path d="M3.5 7l8.5 6 8.5-6" stroke="#c0272d" stroke-width="1.6" fill="none"/></svg></span>
          www.frontdesk@harborlightvitalitystudio.com
        </li>
        <li>
          <span class="icon"><svg viewBox="0 0 24 24"><g fill="none" stroke="#fff" stroke-width="1.8"><circle cx="12" cy="12" r="8.5"/><ellipse cx="12" cy="12" rx="3.8" ry="8.5"/><path d="M3.5 12h17"/></g></svg></span>
          www.harborlightvitalitystudio.com
        </li>
      </ul>
    </div>
    <svg class="swoosh" viewBox="0 0 640 110" preserveAspectRatio="none" aria-hidden="true">
      <path d="M0 110 L0 96 C200 100 420 80 640 18 L640 110 Z" fill="var(--brand-blue)"/>
      <path d="M0 88 C210 92 420 70 640 6 L640 12 C420 78 210 98 0 94 Z" fill="var(--brand-red)"/>
    </svg>
  </section>
</main>
</body>
</html>
```